Vela Link and Wire post card design

We need a postcard to hand out to prospective clients detailing what we do with contact details kept to just a mobile phone number.
Vela Link and Wire is a communications networking company specialising in computer cabling, phone cabling, fibre optics, CCTV, particularly for small business. We offer licenced technicians with over 20 years experience in this field. We service greater Brisbane. Designs that incorporate colours from our logo would be great and that is similar to our business card.
Communications

```html
<!DOCTYPE html>
<html lang="en">
<head>
<meta charset="utf-8">
<title>Vela Link and Wire – Postcard</title>
<link href="https://fonts.googleapis.com/css2?family=Lato:wght@700;900&family=Libre+Baskerville:wght@700&family=Teko:wght@500&display=swap" rel="stylesheet">
<style>
  :root {
    --page: #e6e6e4;
    --ink-dark: #0b0b0b;
    --ember: #c2401c;
    --ember-deep: #5a160a;
    --ember-glow: #f08a4a;
    --green: #5cbf3a;
    --green-light: #8ed96a;
    --green-dark: #3e9a22;
    --white: #ffffff;
    --rule: #6f6f6f;
    --frame: #a8a8a8;
  }
  * { box-sizing: border-box; margin: 0; padding: 0; }
  html, body { width: 806px; height: 1200px; overflow: hidden; }
  body { background: var(--page); position: relative; font-family: "Lato", sans-serif; }

  .card { position: absolute; left: 40px; width: 726px; height: 540px; overflow: hidden; box-shadow: 0 4px 14px rgba(0,0,0,.25); }
  .card--front { top: 36px; background: var(--ink-dark); }
  .card--back { top: 624px; background: var(--white); }

  .fireworks-photo {
    position: absolute; inset: 0;
    background:
      radial-gradient(circle at 22% 25%, var(--ember-glow) 0%, var(--ember) 22%, var(--ember-deep) 48%, transparent 70%),
      radial-gradient(circle at 85% 95%, var(--ember) 0%, var(--ember-deep) 30%, transparent 55%),
      radial-gradient(circle at 10% 90%, var(--ember-deep) 0%, transparent 45%),
      var(--ink-dark);
  }
  .front-panel {
    position: absolute; top: 0; right: 0; width: 336px; height: 320px;
    background: linear-gradient(90deg, rgba(11,11,11,0) 0%, var(--ink-dark) 18%);
  }

  .brand { position: absolute; top: 62px; right: 34px; display: flex; align-items: center; gap: 10px; }
  .brand__dot { width: 22px; height: 22px; border-radius: 50%; background: var(--green); }
  .brand__name { font-family: "Lato", sans-serif; font-weight: 900; font-size: 26px; color: var(--green); }

  .contact { position: absolute; color: var(--white); }
  .contact__name { font-family: "Libre Baskerville", serif; font-weight: 700; }
  .contact__row { display: flex; align-items: center; gap: 10px; }
  .contact__phone { font-family: "Lato", sans-serif; font-weight: 700; }
  .contact__email { font-family: "Libre Baskerville", serif; font-weight: 700; }
  .icon { display: block; flex: none; }

  .front-contact { right: 34px; top: 150px; text-align: right; }
  .front-contact .contact__name { font-size: 32px; margin-bottom: 8px; }
  .front-contact .contact__phone { font-size: 37px; }
  .front-contact .contact__row { justify-content: flex-end; }
  .front-contact .contact__row--email { margin-top: 10px; gap: 24px; }
  .front-contact .contact__email { font-size: 15px; }

  .experience-band {
    position: absolute; left: 50px; top: 356px; width: 622px; height: 100px;
    border-radius: 50px; border: 4px solid #d9d9d9;
    background: linear-gradient(180deg, var(--green-light) 0%, var(--green) 45%, var(--green-dark) 100%);
    box-shadow: 0 3px 8px rgba(0,0,0,.5);
    display: flex; flex-direction: column; align-items: center; justify-content: center;
    font-family: "Teko", sans-serif; font-weight: 500; color: var(--white); line-height: .9;
    text-transform: uppercase;
  }
  .experience-band__lead { font-size: 44px; }
  .experience-band__years { font-size: 34px; }

  .back-photo { position: absolute; left: 0; top: 0; width: 312px; height: 100%; }
  .back-photo .fireworks-photo {
    background:
      radial-gradient(circle at 30% 12%, var(--ember-glow) 0%, var(--ember) 18%, var(--ember-deep) 40%, transparent 60%),
      radial-gradient(circle at 75% 80%, var(--ember) 0%, var(--ember-deep) 30%, transparent 55%),
      var(--ink-dark);
  }
  .divider-stripe { position: absolute; left: 312px; top: 0; width: 14px; height: 100%; background: var(--green); }

  .back-contact { left: 18px; top: 160px; width: 280px; }
  .back-contact .contact__name { font-size: 27px; margin-bottom: 8px; }
  .back-contact .contact__phone { font-size: 31px; }
  .back-contact .contact__row--email { margin-top: 10px; }
  .back-contact .contact__email { font-size: 12.5px; }
  .company-summary {
    margin-top: 16px; font-family: "Libre Baskerville", serif; font-weight: 700;
    font-size: 12.5px; line-height: 1.2;
  }

  .stamp-box { position: absolute; right: 52px; top: 56px; width: 80px; height: 80px; border: 1px solid var(--frame); }
  .address-line { position: absolute; left: 348px; width: 300px; height: 1px; background: var(--rule); }
  .address-line--1 { top: 162px; }
  .address-line--2 { top: 194px; }
  .address-line--3 { top: 226px; }
</style>
</head>
<body>

<section class="card card--front" aria-label="Postcard front">
  <div class="fireworks-photo" role="img" aria-label="Red and orange fireworks bursting against a night sky"></div>
  <div class="front-panel"></div>

  <div class="brand">
    <span class="brand__dot"></span>
    <span class="brand__name">Vela Link and Wire</span>
  </div>

  <div class="contact front-contact">
    <p class="contact__name">Daniel Rourke</p>
    <div class="contact__row">
      <svg class="icon" width="30" height="30" viewBox="0 0 30 30" aria-hidden="true">
        <rect width="30" height="30" rx="5" fill="#5cbf3a"/>
        <path d="M11 6c1 0 2 3 2.5 4.5.3 1-1.5 2-1.5 2.5 0 1.5 3 5 4.5 5 .5 0 1.5-1.8 2.5-1.5C20.5 17 24 18 24 19c0 2-2 4-4 4C13 23 7 16 7 10c0-2 2-4 4-4z" fill="#fff"/>
      </svg>
      <span class="contact__phone">0412-389-205</span>
    </div>
    <div class="contact__row contact__row--email">
      <svg class="icon" width="30" height="18" viewBox="0 0 30 18" aria-hidden="true">
        <rect width="30" height="18" fill="#5cbf3a"/>
        <path d="M1 1l14 10L29 1" fill="none" stroke="#fff" stroke-width="2"/>
      </svg>
      <span class="contact__email">daniel@velalinkwire.com</span>
    </div>
  </div>

  <div class="experience-band">
    <span class="experience-band__lead">Licenced technician with over</span>
    <span class="experience-band__years">25 years experience</span>
  </div>
</section>

<section class="card card--back" aria-label="Postcard back">
  <div class="back-photo">
    <div class="fireworks-photo" role="img" aria-label="Red and orange fireworks bursting against a night sky"></div>
  </div>
  <div class="divider-stripe"></div>

  <div class="contact back-contact">
    <p class="contact__name">Daniel Rourke</p>
    <div class="contact__row">
      <svg class="icon" width="28" height="28" viewBox="0 0 30 30" aria-hidden="true">
        <rect width="30" height="30" rx="5" fill="#5cbf3a"/>
        <path d="M11 6c1 0 2 3 2.5 4.5.3 1-1.5 2-1.5 2.5 0 1.5 3 5 4.5 5 .5 0 1.5-1.8 2.5-1.5C20.5 17 24 18 24 19c0 2-2 4-4 4C13 23 7 16 7 10c0-2 2-4 4-4z" fill="#fff"/>
      </svg>
      <span class="contact__phone">0412-389-205</span>
    </div>
    <div class="contact__row contact__row--email">
      <svg class="icon" width="28" height="16" viewBox="0 0 30 18" aria-hidden="true">
        <rect width="30" height="18" fill="#5cbf3a"/>
        <path d="M1 1l14 10L29 1" fill="none" stroke="#fff" stroke-width="2"/>
      </svg>
      <span class="contact__email">daniel@velalinkwire.com</span>
    </div>
    <p class="company-summary">Vela Link and Wire is a communications networking company specialising in computer cabling, phone cabling, fibre optics, CCTV, particularly for small business.</p>
  </div>

  <div class="stamp-box"></div>
  <div class="address-line address-line--1"></div>
  <div class="address-line address-line--2"></div>
  <div class="address-line address-line--3"></div>
</section>

</body>
</html>
```